Email Signature & Facebook Cover Design – Birchlane Study Centre

I’m looking for a clean, professional email signature and a matching Facebook cover photo for my tutoring business, Birchlane Study Centre.
The email signature needs to display properly across Outlook and iPhone without the image appearing as an attachment. It should include my logo and contact details and have a friendly but professional look suitable for an education business.
Details to include:
Moira Dunholt
Director & Lead Tutor
Birchlane Study Centre
hello@birchlanestudy.co.uk
www.birchlanestudy.co.uk
01632 418736
The Facebook cover should match the branding, feel professional and welcoming, and be optimised for desktop and mobile.

```html
<!DOCTYPE html>
<html lang="en">
<head>
<meta charset="utf-8">
<title>Birchlane Study Centre – Email Signature &amp; Facebook Cover</title>
<link href="https://fonts.googleapis.com/css2?family=Outfit:wght@400;500;600;700;800&family=Bitter:wght@400;500&family=Kaushan+Script&display=swap" rel="stylesheet">
<style>
  :root{
    --board:#323132;
    --label:#6d6c6d;
    --green:#5acb7a;
    --green-deep:#4fbf6e;
    --lime:#c6fa5f;
    --ink:#1e1f22;
    --white:#ffffff;
    --photo-top:#7fd897;
    --photo-bottom:#c9d9ea;
  }
  *{margin:0;padding:0;box-sizing:border-box}
  html,body{width:1200px;height:1053px;overflow:hidden;background:var(--board);font-family:"Outfit",sans-serif}
  .board{position:relative;width:1200px;height:1053px}
  .board-label{position:absolute;left:0;width:1200px;text-align:center;color:var(--label);font-size:13px;font-weight:400;letter-spacing:.3px}
  .panel{position:absolute;left:54px;width:1092px;background:var(--green);overflow:hidden;box-shadow:0 10px 24px rgba(0,0,0,.35)}
  .panel > *{position:absolute}
  .panel-shapes{left:0;top:0}
  .signature{top:100px;height:277px}
  .cover{top:470px;height:404px}

  .brand-name{color:var(--white);font-weight:800;line-height:.92;letter-spacing:-1px}
  .name-row{display:flex;align-items:center;gap:8px;white-space:nowrap}
  .person-name{color:var(--white);font-weight:800;font-size:26px;letter-spacing:.4px;line-height:1}
  .role-pill{background:var(--lime);color:var(--ink);font-weight:600;font-size:11px;padding:2px 6px;border-radius:4px;line-height:1.15;margin-top:4px}
  .contact{display:flex;gap:6px;align-items:flex-start;color:var(--white)}
  .contact-icon{flex:none;border-radius:50%;background:var(--lime);display:flex;align-items:center;justify-content:center}
  .contact-label{font-weight:700;line-height:1.1;display:block}
  .contact-value{font-weight:500;line-height:1.3;display:block}

  .arch{border:10px solid var(--white);border-bottom:none;border-radius:999px 999px 0 0;background:linear-gradient(180deg,var(--photo-top),var(--photo-bottom))}
  .tutor-chip{background:rgba(255,255,255,.92);border-radius:20px;display:flex;align-items:center;gap:5px;padding:0 8px 0 4px}
  .chip-avatar{border-radius:50%;background:#c9a58f;flex:none}
  .chip-name{font-weight:700;color:var(--ink);line-height:1;display:block}
  .chip-role{font-weight:400;color:#777;line-height:1.2;display:block}

  .social-band{background:var(--ink);border-top-left-radius:80px;display:flex;align-items:center;color:var(--white);font-weight:500}
  .social-dot{border-radius:50%;background:var(--white);flex:none}

  .tagline{font-family:"Bitter",serif;color:var(--white);font-weight:400;line-height:1.1}
  .tagline-script{font-family:"Kaushan Script",cursive;display:block;line-height:1.05}
</style>
</head>
<body>
<main class="board">

  <p class="board-label" style="top:64px">Email Signature</p>

  <section class="panel signature" aria-label="Email signature">
    <svg class="panel-shapes" width="1092" height="277" viewBox="0 0 1092 277" aria-hidden="true">
      <path d="M0 0H100C96 30 70 50 45 62C25 72 10 80 0 75Z" fill="var(--lime)"/>
      <circle cx="55" cy="63" r="21" fill="none" stroke="var(--white)" stroke-width="4"/>
      <path d="M948 0H1092V146C1060 150 1025 140 1010 110C995 80 990 40 948 0Z" fill="var(--lime)"/>
      <path d="M755 290L790 250C810 228 830 205 850 183" stroke="var(--lime)" stroke-width="9" fill="none" stroke-linecap="round"/>
      <rect x="842" y="48" width="32" height="32" rx="4" transform="rotate(45 858 64)" fill="var(--lime)"/>
    </svg>

    <p class="brand-name" style="left:119px;top:88px;font-size:50px">Birchlane<br><span style="font-size:34px">Study Centre</span></p>

    <div class="name-row" style="left:357px;top:82px">
      <h1 class="person-name">MOIRA DUNHOLT</h1>
      <p class="role-pill">Director &amp; Lead Tutor Birchlane Study Centre</p>
    </div>

    <div class="contact" style="left:356px;top:136px;font-size:11px">
      <span class="contact-icon" style="width:17px;height:17px"><svg width="9" height="9" viewBox="0 0 24 24"><path d="M6 2l4 5-2 3c1 3 3 5 6 6l3-2 5 4-3 4C10 22 2 14 2 5z" fill="var(--green)"/></svg></span>
      <span><span class="contact-label" style="font-size:12px">Phone</span><span class="contact-value">01632 418736</span></span>
    </div>
    <div class="contact" style="left:485px;top:136px;font-size:11px">
      <span class="contact-icon" style="width:17px;height:17px"><svg width="10" height="8" viewBox="0 0 24 18"><rect x="1" y="1" width="22" height="16" rx="2" fill="var(--green)"/><path d="M2 3l10 7 10-7" stroke="var(--lime)" stroke-width="2" fill="none"/></svg></span>
      <span><span class="contact-label" style="font-size:12px">Email</span><span class="contact-value">hello@birchlanestudy.co.uk</span></span>
    </div>
    <div class="contact" style="left:356px;top:186px;font-size:11px">
      <span class="contact-icon" style="width:17px;height:17px"><svg width="10" height="10" viewBox="0 0 24 24"><circle cx="12" cy="12" r="10" fill="none" stroke="var(--green)" stroke-width="3"/><path d="M2 12h20M12 2c4 4 4 16 0 20M12 2c-4 4-4 16 0 20" stroke="var(--green)" stroke-width="2" fill="none"/></svg></span>
      <span><span class="contact-label" style="font-size:12px">Website</span><span class="contact-value">www.birchlanestudy.co.uk</span></span>
    </div>

    <div class="arch" role="img" aria-label="Photo of a smiling tutor with a laptop" style="left:848px;top:20px;width:200px;height:240px"></div>
    <div class="tutor-chip" style="left:876px;top:71px;height:30px">
      <span class="chip-avatar" style="width:20px;height:20px" role="img" aria-label="Tutor avatar"></span>
      <span><span class="chip-name" style="font-size:8px">Ms Harlow</span><span class="chip-role" style="font-size:5px">English Tutor</span></span>
    </div>

    <div class="social-band" style="left:810px;top:230px;width:282px;height:47px;padding-left:88px;gap:7px;font-size:10px">
      <span class="social-dot" style="width:14px;height:14px"></span>
      <span class="social-dot" style="width:14px;height:14px"></span>
      <span class="social-dot" style="width:14px;height:14px"></span>
      <span class="social-dot" style="width:14px;height:14px"></span>
      <span style="margin-left:9px">@username</span>
    </div>
  </section>

  <p class="board-label" style="top:432px">Facebook Cover</p>

  <section class="panel cover" aria-label="Facebook cover">
    <svg class="panel-shapes" width="1092" height="404" viewBox="0 0 1092 404" aria-hidden="true">
      <path d="M0 0H113C110 40 85 80 50 100C30 110 12 112 0 110Z" fill="var(--lime)"/>
      <circle cx="53" cy="96" r="19" fill="none" stroke="var(--white)" stroke-width="4"/>
      <path d="M929 0H1092V242C1060 245 1030 230 1015 200C995 160 1000 90 975 50C965 30 950 15 929 0Z" fill="var(--lime)"/>
      <path d="M642 420L690 360C715 328 735 300 760 270" stroke="var(--lime)" stroke-width="12" fill="none" stroke-linecap="round"/>
      <circle cx="775" cy="112" r="28" fill="var(--lime)"/>
    </svg>

    <p class="brand-name" style="left:108px;top:80px;font-size:48px">Birchlane<br><span style="font-size:33px">Study Centre</span></p>

    <div class="contact" style="left:106px;top:250px;font-size:9.5px">
      <span class="contact-icon" style="width:15px;height:15px"><svg width="8" height="8" viewBox="0 0 24 24"><path d="M6 2l4 5-2 3c1 3 3 5 6 6l3-2 5 4-3 4C10 22 2 14 2 5z" fill="var(--green)"/></svg></span>
      <span><span class="contact-label" style="font-size:11px">Phone</span><span class="contact-value">01632 418736</span></span>
    </div>
    <div class="contact" style="left:225px;top:250px;font-size:9.5px">
      <span class="contact-icon" style="width:15px;height:15px"><svg width="9" height="7" viewBox="0 0 24 18"><rect x="1" y="1" width="22" height="16" rx="2" fill="var(--green)"/><path d="M2 3l10 7 10-7" stroke="var(--lime)" stroke-width="2" fill="none"/></svg></span>
      <span><span class="contact-label" style="font-size:11px">Email</span><span class="contact-value">hello@birchlanestudy.co.uk</span></span>
    </div>
    <div class="contact" style="left:106px;top:303px;font-size:9.5px">
      <span class="contact-icon" style="width:15px;height:15px"><svg width="9" height="9" viewBox="0 0 24 24"><circle cx="12" cy="12" r="10" fill="none" stroke="var(--green)" stroke-width="3"/><path d="M2 12h20M12 2c4 4 4 16 0 20M12 2c-4 4-4 16 0 20" stroke="var(--green)" stroke-width="2" fill="none"/></svg></span>
      <span><span class="contact-label" style="font-size:11px">Website</span><span class="contact-value">www.birchlanestudy.co.uk</span></span>
    </div>

    <h2 class="tagline" style="left:440px;top:72px;font-size:52px">
      Learning<br>that clicks,<br><span class="tagline-script" style="font-size:52px">confidence</span>that truly<br>sticks.
    </h2>

    <div class="arch" role="img" aria-label="Photo of a smiling tutor with a laptop" style="left:758px;top:56px;width:274px;height:300px;border-width:13px"></div>
    <div class="tutor-chip" style="left:788px;top:123px;height:40px">
      <span class="chip-avatar" style="width:28px;height:28px" role="img" aria-label="Tutor avatar"></span>
      <span><span class="chip-name" style="font-size:10px">Ms Harlow</span><span class="chip-role" style="font-size:6px">English Tutor</span></span>
    </div>

    <div class="social-band" style="left:711px;top:338px;width:381px;height:66px;padding-left:59px;gap:14px;font-size:15px;border-top-left-radius:100px">
      <span class="social-dot" style="width:22px;height:22px"></span>
      <span class="social-dot" style="width:22px;height:22px"></span>
      <span class="social-dot" style="width:22px;height:22px"></span>
      <span class="social-dot" style="width:22px;height:22px"></span>
      <span style="margin-left:6px">@username</span>
    </div>
  </section>

</main>
</body>
</html>
```